Sumvane financial services stationery design

We need business stationery designed with letterheads, business cards, with compliments and envelope for a business that offers tax and accounting services

Designs look the same

Target Market(s)

Small to medium businesses, individuals, Self managed superfunds

Industry/Entity Type

Business

Font styles to use
Serif
Other font styles liked:
• Atlanta

Colors
32a6d6
3277b5

Requirements
Must have
• Logo incorporated with all my stationery
• professional
Should not have
• Lots of colours
• Busy

```html
<!DOCTYPE html>
<html lang="en">
<head>
<meta charset="utf-8">
<title>Sumvane Financial Services – Stationery</title>
<link rel="stylesheet" href="https://fonts.googleapis.com/css2?family=Open+Sans:wght@400;600&display=swap">
<style>
  :root{
    --sky:#32a6d6;
    --ocean:#3277b5;
    --ink:#333740;
    --muted:#5a5f66;
    --paper:#ffffff;
    --backdrop:#e6e8eb;
    --rule:#cfd3d8;
  }
  *{box-sizing:border-box;margin:0;padding:0}
  html,body{width:1200px;height:1200px;overflow:hidden}
  body{background:var(--backdrop);font-family:"Open Sans",Arial,sans-serif;color:var(--ink);position:relative}
  .sheet{position:absolute;background:var(--paper);box-shadow:0 2px 8px rgba(0,0,0,.12)}
  .brand{display:flex;align-items:center;gap:10px}
  .brand-square{background:var(--sky);flex:none}
  .brand-name{font-family:"Open Sans",Arial,sans-serif;font-weight:600;color:var(--ocean);text-transform:uppercase;letter-spacing:.06em;line-height:1;white-space:nowrap}
  .icon{display:inline-block;vertical-align:middle;fill:var(--ocean);flex:none}

  /* Letterhead */
  .letterhead{left:40px;top:133px;width:660px;height:933px}
  .letterhead .brand{position:absolute;left:32px;top:30px}
  .letterhead .brand-square{width:56px;height:56px}
  .letterhead .brand-name{font-size:34px}
  .recipient{position:absolute;left:49px;top:214px;font-size:11.5px;line-height:26px}
  .letter-body{position:absolute;left:49px;top:320px;width:560px;font-size:11.5px;line-height:26px}
  .letter-body p{margin-bottom:20px}
  .closing{position:absolute;left:53px;top:633px;font-size:11.5px}
  .signature{position:absolute;left:50px;top:665px;width:110px;height:36px;background:linear-gradient(90deg,rgba(50,119,181,.25),rgba(50,166,214,.12));border-radius:4px}
  .letter-contact{position:absolute;left:485px;top:760px;font-size:13px;line-height:16px;color:var(--muted)}
  .letter-contact li{list-style:none;display:flex;gap:5px;align-items:flex-start}
  .letter-contact .gap{margin-top:4px}

  /* Business cards */
  .card{width:205px;height:117px;top:307px}
  .card-front{left:740px}
  .card-back{left:955px}
  .card-front .brand{position:absolute;left:16px;top:48px;gap:5px}
  .card-front .brand-square{width:18px;height:18px}
  .card-front .brand-name{font-size:11px;letter-spacing:.04em}
  .card-front .divider{position:absolute;left:114px;top:30px;width:1px;height:60px;background:var(--ocean)}
  .card-details{position:absolute;left:120px;top:30px;font-size:5.5px;line-height:7.5px;color:var(--muted)}
  .card-details .holder{font-size:9px;line-height:11px;font-weight:600;color:var(--sky)}
  .card-details .role{margin-bottom:5px}
  .card-details li{list-style:none;display:flex;gap:3px}
  .card-back .brand{position:absolute;left:0;right:0;top:40px;justify-content:center;gap:8px}
  .card-back .brand-square{width:24px;height:24px}
  .card-back .brand-name{font-size:16px}
  .card-back .site{position:absolute;left:0;right:0;top:92px;text-align:center;font-size:8px;letter-spacing:.12em;color:var(--muted)}

  /* Compliments slip */
  .slip{left:740px;top:454px;width:420px;height:198px}
  .slip .brand{position:absolute;left:24px;top:20px;gap:8px}
  .slip .brand-square{width:32px;height:32px}
  .slip .brand-name{font-size:20px}
  .slip-contact{position:absolute;left:28px;top:64px;font-size:6.5px;line-height:9.5px;color:var(--muted)}
  .slip-contact li{list-style:none;display:flex;gap:3px;align-items:center}
  .slip-title{position:absolute;right:22px;top:150px;font-size:18px;letter-spacing:.1em;color:var(--ocean)}

  /* Envelope */
  .envelope{left:740px;top:682px;width:420px;height:210px}
  .envelope .brand{position:absolute;left:24px;top:20px;gap:8px}
  .envelope .brand-square{width:32px;height:32px}
  .envelope .brand-name{font-size:20px}
  .envelope-return{position:absolute;left:28px;top:64px;font-size:6.5px;color:var(--muted);display:flex;gap:3px;align-items:center}
</style>
</head>
<body>

<svg width="0" height="0" style="position:absolute" aria-hidden="true">
  <defs>
    <symbol id="i-phone" viewBox="0 0 16 16"><path d="M2 5c0-2 2-3 6-3s6 1 6 3v2h-3V5.5H5V7H2zM4 8h8l2 6H2z"/></symbol>
    <symbol id="i-globe" viewBox="0 0 16 16"><circle cx="8" cy="8" r="7" fill="none" stroke="currentColor" stroke-width="1.6"/><path d="M1 8h14M8 1c-3 3-3 11 0 14M8 1c3 3 3 11 0 14" fill="none" stroke="currentColor" stroke-width="1.2"/></symbol>
    <symbol id="i-mail" viewBox="0 0 16 16"><path d="M1 3h14v10H1z"/><path d="M1 3l7 6 7-6" fill="none" stroke="#fff" stroke-width="1.2"/></symbol>
    <symbol id="i-pin" viewBox="0 0 16 16"><path d="M8 1a5 5 0 0 0-5 5c0 4 5 9 5 9s5-5 5-9a5 5 0 0 0-5-5zm0 7a2 2 0 1 1 0-4 2 2 0 0 1 0 4z"/></symbol>
  </defs>
</svg>

<!-- Letterhead -->
<section class="sheet letterhead">
  <div class="brand"><span class="brand-square"></span><span class="brand-name">Sumvane</span></div>
  <div class="recipient">To<br>The,<br>Director</div>
  <div class="letter-body">
    <p>Lorem ipsum dolor sit amet, consectetur adipiscing elit. Integer nec odio, praesent libero sed cursus ante dictum, massa quam dapibus leo, eget vulputate nisi enim at purus. Nulla quis sem at nibh elementum aliquam quam vel dolor. Nunc adipiscing. Sed vel lectus donec odio tempus molestie porttitor. Vestibulum ut nulla aliquam risus rutrum interdum sit amet nec ante.</p>
    <p>Curabitur sit amet erat quis risus feugiat viverra. Pellentesque augue justo, sagittis et, lacinia at, venenatis non, arcu. Nunc nec libero. In cursus dictum justo, quis dignissim sem commodo eu. Duis dolor dolor, nunc, egestas at, accumsan at, malesuada vel, velit. Vestibulum ante ipsum primis in faucibus orci luctus et ultrices posuere cubilia curae; aenean vehicula. Nullam quis enim. Integer dignissim viverra velit.</p>
  </div>
  <div class="closing">Thanking you,</div>
  <div class="signature" role="img" aria-label="Handwritten signature of Mara Lind"></div>
  <ul class="letter-contact">
    <li><svg class="icon" width="11" height="11"><use href="#i-phone"/></svg>123-456-7890</li>
    <li><svg class="icon" width="11" height="11" style="color:var(--ocean)"><use href="#i-globe"/></svg>www.sumvane.com</li>
    <li><svg class="icon" width="11" height="11"><use href="#i-mail"/></svg>mara@sumvane.com</li>
    <li class="gap"><svg class="icon" width="11" height="11"><use href="#i-pin"/></svg>Dummy city<br>Dummy country, land</li>
  </ul>
</section>

<!-- Business card, front -->
<section class="sheet card card-front">
  <div class="brand"><span class="brand-square"></span><span class="brand-name">Sumvane</span></div>
  <div class="divider"></div>
  <div class="card-details">
    <div class="holder">MARA LIND</div>
    <div class="role">Director</div>
    <ul>
      <li><svg class="icon" width="5" height="6"><use href="#i-pin"/></svg>Dummy city<br>Dummy country, land</li>
      <li><svg class="icon" width="5" height="6"><use href="#i-phone"/></svg>123-456-7890</li>
      <li><svg class="icon" width="5" height="6" style="color:var(--ocean)"><use href="#i-globe"/></svg>www.sumvane.com</li>
      <li><svg class="icon" width="5" height="6"><use href="#i-mail"/></svg>mara@sumvane.com</li>
    </ul>
  </div>
</section>

<!-- Business card, back -->
<section class="sheet card card-back">
  <div class="brand"><span class="brand-square"></span><span class="brand-name">Sumvane</span></div>
  <div class="site">www.sumvane.com</div>
</section>

<!-- With compliments slip -->
<section class="sheet slip">
  <div class="brand"><span class="brand-square"></span><span class="brand-name">Sumvane</span></div>
  <ul class="slip-contact">
    <li><svg class="icon" width="6" height="6"><use href="#i-phone"/></svg>123-456-7890</li>
    <li><svg class="icon" width="6" height="6" style="color:var(--ocean)"><use href="#i-globe"/></svg>www.sumvane.com&nbsp;|&nbsp;<svg class="icon" width="6" height="6"><use href="#i-mail"/></svg>mara@sumvane.com</li>
    <li><svg class="icon" width="6" height="6"><use href="#i-pin"/></svg>Dummy city, Dummy country, land</li>
  </ul>
  <div class="slip-title">WITH COMPLEMENTS</div>
</section>

<!-- Envelope -->
<section class="sheet envelope">
  <div class="brand"><span class="brand-square"></span><span class="brand-name">Sumvane</span></div>
  <div class="envelope-return"><svg class="icon" width="6" height="6"><use href="#i-pin"/></svg>Dummy city, Dummy country, land</div>
</section>

</body>
</html>
```